TRU PEAK POWER.

I'd like my business logo.
contact name: Desmond Halvik
phone:0438275160
email: info@trupeakpower.net.au
website: www.trupeakpower.net.au

services:
solar
battery storage
LED lighting
energy saving solutions
general electrical
I'd like the design to look professional

Target Market(s)

Everyone

Industry/Entity Type

Business

Contact Information for Business Card

as described above

Requirements
Must have
• Id like the colours and the design to work well with my logo.

```html
<!DOCTYPE html>
<html lang="en">
<head>
<meta charset="utf-8">
<title>Tru Peak Power – Business Card</title>
<link href="https://fonts.googleapis.com/css2?family=Roboto:wght@400;700&display=swap" rel="stylesheet">
<style>
  :root {
    --backdrop: #cdeeed;
    --card-white: #f7f7f5;
    --charcoal: #3b3b3d;
    --orange: #e8722e;
    --orange-dark: #b9541c;
    --green: #62ad3c;
    --text-light: #ffffff;
  }
  html, body {
    margin: 0;
    width: 1200px;
    height: 1104px;
    overflow: hidden;
    background: var(--backdrop);
    font-family: "Roboto", Arial, sans-serif;
  }
  .business-card {
    position: absolute;
    left: 100px;
    top: 266px;
    width: 1000px;
    height: 572px;
    background: var(--card-white);
    overflow: hidden;
    box-shadow: 0 18px 40px rgba(0, 60, 60, 0.18);
  }
  .card-shapes {
    position: absolute;
    inset: 0;
  }
  .brand {
    position: absolute;
    left: 90px;
    top: 162px;
    display: flex;
    align-items: center;
    gap: 16px;
  }
  .brand-dot {
    width: 50px;
    height: 50px;
    border-radius: 50%;
    background: var(--green);
  }
  .brand-name {
    font-weight: 700;
    font-size: 42px;
    color: var(--green);
    letter-spacing: 1px;
    white-space: nowrap;
  }
  .services {
    position: absolute;
    left: 628px;
    top: 58px;
    margin: 0;
    padding: 0;
    list-style: none;
    color: var(--text-light);
    font-size: 20px;
    line-height: 31px;
    text-transform: uppercase;
  }
  .contact-item {
    position: absolute;
    display: flex;
    align-items: center;
    gap: 16px;
    color: var(--text-light);
    font-size: 28px;
    white-space: nowrap;
  }
  .contact-item svg { flex: none; }
  .contact-name  { left: 120px; top: 394px; }
  .contact-phone { left: 120px; top: 454px; }
  .contact-email { left: 530px; top: 394px; }
  .contact-web   { left: 530px; top: 454px; }
</style>
</head>
<body>
  <section class="business-card">
    <svg class="card-shapes" width="1000" height="572" viewBox="0 0 1000 572" aria-hidden="true">
      <rect class="top-right-block" x="700" y="0" width="300" height="290" fill="var(--charcoal)"/>
      <rect class="services-panel" x="600" y="28" width="220" height="210" fill="var(--orange)"/>
      <polygon class="services-fold" points="790,238 820,238 820,268" fill="var(--orange-dark)"/>
      <path class="orange-swoosh" d="M0 330 C 140 400, 340 330, 700 315 L 700 572 L 0 572 Z" fill="var(--orange)"/>
      <path class="contact-band" d="M0 372 C 160 440, 340 350, 520 330 L 1000 290 L 1000 572 L 0 572 Z" fill="var(--charcoal)"/>
    </svg>

    <div class="brand">
      <span class="brand-dot"></span>
      <span class="brand-name">TRU PEAK POWER</span>
    </div>

    <ul class="services">
      <li>Solar</li>
      <li>Battery Storage</li>
      <li>LED Lighting</li>
      <li>Energy Saving</li>
      <li>Solutions</li>
    </ul>

    <div class="contact-item contact-name">
      <svg width="18" height="26" viewBox="0 0 18 26"><circle cx="9" cy="6" r="5" fill="var(--green)"/><path d="M1 25 C1 14, 17 14, 17 25 Z" fill="var(--green)"/></svg>
      <span>Desmond Halvik</span>
    </div>
    <div class="contact-item contact-phone">
      <svg width="22" height="22" viewBox="0 0 24 24"><path d="M6.6 10.8a15 15 0 0 0 6.6 6.6l2.2-2.2a1 1 0 0 1 1-.25 11.4 11.4 0 0 0 3.6.6 1 1 0 0 1 1 1V20a1 1 0 0 1-1 1A17 17 0 0 1 3 4a1 1 0 0 1 1-1h3.5a1 1 0 0 1 1 1c0 1.25.2 2.45.6 3.6a1 1 0 0 1-.25 1z" fill="var(--green)"/></svg>
      <span>0438 275 160</span>
    </div>
    <div class="contact-item contact-email">
      <svg width="24" height="18" viewBox="0 0 24 18"><rect x="0" y="0" width="24" height="18" rx="2" fill="var(--green)"/><path d="M1 1 L12 10 L23 1" stroke="var(--charcoal)" stroke-width="2" fill="none"/></svg>
      <span>info@trupeakpower.net.au</span>
    </div>
    <div class="contact-item contact-web">
      <svg width="24" height="24" viewBox="0 0 24 24"><circle cx="12" cy="12" r="11" fill="var(--green)"/><path d="M1 12h22M12 1c4 4 4 18 0 22M12 1c-4 4-4 18 0 22" stroke="var(--charcoal)" stroke-width="1.6" fill="none"/></svg>
      <span>www.trupeakpower.net.au</span>
    </div>
  </section>
</body>
</html>
```